Newsletter masthead

We need a masthead for the cover page of our A4 newsletter. It must be 4-5 cms (height) and to fit the whole width of an A4 paper (21cms).

We are a research centre focused on men’s health e.g. male ageing, male obesity and diabetes, prostate cancer research, and male mental health. Our primary readers are researchers, academics, and members of the community.

We’d like to see a masthead that complements our organisation logo (please see attached BTCMH logo). Please note that our Centre logo will be used elsewhere in our newsletter so please do not include the logo in the masthead.

Please include the following words in the masthead:

Vantara (name of the newsletter) – please emphasize the ‘men’ part of Vantara, if possible.

Advancing research into men’s wellbeing (subtitle of the newsletter)

A Newsletter of the Bellridge Trust Centre for Men’s Health (origin of the newsletter)

We would like to avoid heavy use of a 3-D effect. We want to keep it simple but modern.

Please note that our Centre logo (attached as BTCMH logo) will be used elsewhere in our newsletter. Please do not include the logo in the masthead. Thank you so much. 

Industry/Entity Type

Health

Requirements
Nice to have
• The masthead could compliment our Centre's logo (please see attached).

Masthead could convey speed or momentum.
Should not have
• Our Centre's logo.

```html
<!DOCTYPE html>
<html lang="en">
<head>
<meta charset="utf-8">
<title>Vantara — Newsletter Masthead</title>
<link href="https://fonts.googleapis.com/css2?family=Roboto:ital,wght@0,300;0,500;1,400;1,700&display=swap" rel="stylesheet">
<style>
  :root {
    --page-bg: #ffffff;
    --band-dark: #333435;
    --band-mid: #4a4b4c;
    --band-light: #5a5b5c;
    --type-white: #ffffff;
    --type-soft: #e6e6e6;
    --accent-green: #1f7a3c;
    --rule-grey: #6d6e6f;
  }
  html, body {
    margin: 0;
    padding: 0;
    width: 1200px;
    height: 900px;
    overflow: hidden;
    background: var(--page-bg);
  }
  .canvas {
    position: relative;
    width: 1200px;
    height: 900px;
  }
  .masthead {
    position: absolute;
    left: 90px;
    top: 344px;
    width: 1006px;
    height: 222px;
    overflow: hidden;
    background: linear-gradient(100deg, var(--band-dark) 0%, var(--band-mid) 55%, var(--band-light) 100%);
    box-shadow: 0 3px 8px rgba(0, 0, 0, 0.35);
  }
  .masthead svg {
    display: block;
    width: 1006px;
    height: 222px;
  }
  .masthead-title {
    font-family: "Roboto", Arial, sans-serif;
    font-style: normal;
    font-weight: 300;
    font-size: 104px;
    letter-spacing: 18px;
    fill: var(--type-white);
  }
  .masthead-subtitle {
    font-family: "Roboto", Arial, sans-serif;
    font-style: italic;
    font-weight: 700;
    font-size: 22px;
    fill: var(--type-white);
  }
  .masthead-origin {
    font-family: "Roboto", Arial, sans-serif;
    font-style: italic;
    font-weight: 400;
    font-size: 12.5px;
    letter-spacing: 0.3px;
    fill: var(--type-soft);
  }
</style>
</head>
<body>
  <div class="canvas">
    <header class="masthead">
      <svg viewBox="0 0 1006 222" xmlns="http://www.w3.org/2000/svg">
        <defs>
          <linearGradient id="speed-rule" x1="0" y1="0" x2="1" y2="0">
            <stop offset="0" stop-color="var(--accent-green)"/>
            <stop offset="0.62" stop-color="var(--accent-green)"/>
            <stop offset="0.72" stop-color="var(--rule-grey)"/>
            <stop offset="1" stop-color="var(--rule-grey)" stop-opacity="0.4"/>
          </linearGradient>
        </defs>
        <text class="masthead-title" x="30" y="116">VANTARA</text>
        <text class="masthead-subtitle" x="34" y="152">ADVANCING RESEARCH INTO MEN’S WELLBEING</text>
        <rect class="speed-rule" x="0" y="172" width="1006" height="3" fill="url(#speed-rule)"/>
        <text class="masthead-origin" x="34" y="199">A NEWSLETTER OF THE BELLRIDGE TRUST CENTRE FOR MEN’S HEALTH</text>
      </svg>
    </header>
  </div>
</body>
</html>
```